Maplecrest Apartments Downtown Northport

We are looking to redesign our entry way sign at Maplecrest Apartments, a low density residential apartment building, located in Downtown Northport, Alabama, U.S. Downtown Northport is a bustling boutique business district with a small town feel comprised of shops, restaurants, and a renowned arts community known for Varrow Arts Center and Festival which is one of the nation's top outdoor arts festivals. Maplecrest Apartments and its sign is the first thing you seen when you enter Downtown Northport. We are looking to redesign our sign, entry way and landscaping to compliment the building and character of the historic downtown.

Target Market(s)

Our apartment building is comprised of 20 apartments units with tenants who are primarily part of the local workforce, young professionals, or students at the Halverton College or other nearby institutions.

Requirements
Must have
• The name of the apartment building - Maplecrest
Phone number on the sign 205-555-0148

```html
<!DOCTYPE html>
<html lang="en">
<head>
<meta charset="utf-8">
<title>Maplecrest Entry Sign</title>
<link href="https://fonts.googleapis.com/css2?family=Montserrat:wght@600;700&display=swap" rel="stylesheet">
<style>
  :root {
    --backdrop-light: #e4e4e4;
    --backdrop-dark: #a9a9a9;
    --slate-deep: #050505;
    --slate-mid: #1c1c1c;
    --letter-stone: #dcdcdc;
    --letter-edge: #6e6e6e;
    --sign-shadow: rgba(0, 0, 0, 0.55);
  }
  * { margin: 0; padding: 0; box-sizing: border-box; }
  html, body {
    width: 998px;
    height: 1200px;
    overflow: hidden;
  }
  body {
    background: radial-gradient(ellipse at 50% 35%, var(--backdrop-light) 0%, var(--backdrop-dark) 100%);
    position: relative;
    font-family: "Montserrat", sans-serif;
  }
  .entry-sign {
    position: absolute;
    left: 76px;
    top: 432px;
    width: 846px;
    height: 338px;
    background:
      radial-gradient(ellipse at 30% 20%, var(--slate-mid) 0%, transparent 60%),
      radial-gradient(ellipse at 80% 85%, #121212 0%, transparent 55%),
      linear-gradient(170deg, #111 0%, var(--slate-deep) 100%);
    box-shadow: 12px 16px 22px var(--sign-shadow);
    display: flex;
    flex-direction: column;
    align-items: center;
    justify-content: center;
    padding-bottom: 20px;
  }
  .building-name {
    color: var(--letter-stone);
    font-weight: 700;
    font-size: 100px;
    letter-spacing: 1px;
    line-height: 1;
    text-shadow: -3px 2px 0 var(--letter-edge), -5px 4px 4px rgba(0,0,0,0.6);
  }
  .phone-line {
    margin-top: 30px;
    display: flex;
    align-items: center;
    gap: 10px;
    color: var(--letter-stone);
    font-weight: 600;
    font-size: 54px;
    line-height: 1;
    text-shadow: -2px 2px 0 var(--letter-edge);
  }
  .phone-icon {
    width: 44px;
    height: 44px;
    fill: var(--letter-stone);
  }
</style>
</head>
<body>
  <div class="entry-sign">
    <h1 class="building-name">MAPLECREST</h1>
    <p class="phone-line">
      <svg class="phone-icon" viewBox="0 0 24 24" aria-hidden="true">
        <path d="M6.6 10.8c1.4 2.8 3.8 5.1 6.6 6.6l2.2-2.2c.3-.3.7-.4 1-.2 1.1.4 2.3.6 3.6.6.6 0 1 .4 1 1V20c0 .6-.4 1-1 1C10.6 21 3 13.4 3 4c0-.6.4-1 1-1h3.5c.6 0 1 .4 1 1 0 1.3.2 2.5.6 3.6.1.3 0 .7-.2 1l-2.3 2.2z"/>
        <path d="M15 3a6 6 0 0 1 6 6h-1.6A4.4 4.4 0 0 0 15 4.6z"/>
        <path d="M15 6.2A2.8 2.8 0 0 1 17.8 9h-1.5A1.3 1.3 0 0 0 15 7.7z"/>
      </svg>
      <span class="phone-number">205 555 0148</span>
    </p>
  </div>
</body>
</html>
```